Business Card Design Project

I have had my current business card for 6years and it is time to upgrade my business card. I have uploaded my old card
I am a retail specialty shop designer and want something designer looking but professional.
Target Market(s)
30-60 year old people in retail businesses
Industry/Entity Type
Retail
Requirements
Must have
- The Maple Fitouts logo (but colour can and style can be altered)
My name, position and contact details as per my existing card attached .
Rowan Pellicott Director
m: 0418593417
rowan@maplefitouts-example.com.au
www.maplefitouts-example.com.au
t:02 95318274 f: 02 95318291
po box 871 fernbrook vale nsw 2190
Nice to have
- Use both sides of the card

```html
<!DOCTYPE html>
<html lang="en">
<head>
<meta charset="utf-8">
<title>Maple Fitouts – Business Card</title>
<link rel="stylesheet" href="https://fonts.googleapis.com/css2?family=Arimo:wght@400&display=swap">
<style>
  :root {
    --page-bg: #2e2e30;
    --card-deep: #0d2a9c;
    --card-mid: #1f4fd0;
    --card-light: #4f97ec;
    --card-glow: #7cc0f6;
    --mark: #141414;
    --text-light: #ffffff;
    --text-soft: #e3efff;
  }
  html, body {
    margin: 0;
    padding: 0;
    width: 1200px;
    height: 456px;
    overflow: hidden;
    background: var(--page-bg);
    font-family: "Arimo", Arial, sans-serif;
  }
  .stage {
    position: relative;
    width: 1200px;
    height: 456px;
  }
  .card {
    position: absolute;
    top: 73px;
    height: 308px;
    border-radius: 20px;
    overflow: hidden;
  }
  .card--front { left: 77px; width: 510px; }
  .card--back { left: 615px; width: 543px; }
  .card__backdrop {
    position: absolute;
    inset: 0;
  }
  .card--front .card__backdrop {
    background:
      radial-gradient(ellipse 55% 45% at 50% 28%, var(--card-light) 0%, transparent 75%),
      radial-gradient(ellipse 70% 50% at 35% 85%, rgba(124,192,246,0.45) 0%, transparent 70%),
      linear-gradient(180deg, var(--card-mid) 0%, var(--card-deep) 100%);
  }
  .card--back .card__backdrop {
    background:
      radial-gradient(ellipse 60% 50% at 20% 25%, var(--card-glow) 0%, transparent 75%),
      radial-gradient(ellipse 50% 45% at 20% 85%, rgba(124,192,246,0.55) 0%, transparent 70%),
      linear-gradient(160deg, var(--card-light) 0%, var(--card-mid) 55%, var(--card-deep) 100%);
  }
  .brand {
    position: absolute;
    display: flex;
    align-items: center;
    gap: 12px;
    color: var(--text-light);
    font-weight: 400;
    text-transform: uppercase;
    letter-spacing: 2px;
    line-height: 1.15;
  }
  .brand__square {
    width: 28px;
    height: 28px;
    background: var(--mark);
    flex: none;
  }
  .card--front .brand {
    left: 50%;
    top: 50%;
    transform: translate(-50%, -50%);
    font-size: 32px;
  }
  .card--back .brand {
    left: 38px;
    top: 160px;
    transform: translateY(-50%);
    font-size: 20px;
  }
  .card--back .brand__square { width: 19px; height: 19px; }
  .contact {
    position: absolute;
    left: 231px;
    top: 68px;
    color: var(--text-light);
  }
  .contact__name {
    margin: 0;
    font-size: 24px;
    font-weight: 400;
    letter-spacing: 0.3px;
    line-height: 28px;
  }
  .contact__role {
    margin: 0;
    font-size: 15px;
    line-height: 18px;
  }
  .contact__details {
    list-style: none;
    margin: 24px 0 0;
    padding: 0;
    font-size: 14.5px;
    line-height: 17px;
    color: var(--text-soft);
  }
</style>
</head>
<body>
<main class="stage">
  <section class="card card--front" aria-label="Card front">
    <div class="card__backdrop" role="img" aria-label="Soft blue bokeh light background"></div>
    <div class="brand">
      <span class="brand__square"></span>
      <span class="brand__name">Maple<br>Fitouts</span>
    </div>
  </section>

  <section class="card card--back" aria-label="Card back">
    <div class="card__backdrop" role="img" aria-label="Soft blue bokeh light background"></div>
    <div class="brand">
      <span class="brand__square"></span>
      <span class="brand__name">Maple<br>Fitouts</span>
    </div>
    <div class="contact">
      <h1 class="contact__name">Rowan Pellicott</h1>
      <p class="contact__role">Director</p>
      <ul class="contact__details">
        <li>PO box 871 fernbrook vale nsw 2190</li>
        <li>M: 0418 593 417</li>
        <li>T: (02) 9531 8274</li>
        <li>F: (02) 9531 8291</li>
        <li>rowan@maplefitouts-example.com.au</li>
        <li>www.maplefitouts-example.com.au</li>
      </ul>
    </div>
  </section>
</main>
</body>
</html>
```